Aged Care Consultancy Business needs a business card design

I need a two sided business card - I want it clean and professional. Surprise me

Target Market(s)

middle aged and ageing victorians

Industry/Entity Type

Health Care

Contact Information for Business Card

Text to be included

Logo
Aged Care Consulting Services
Professional, Reliable, Affordable

Tovan Brelsick
Director
0427 31 64 92 (larger)
1300 73 29 41
tovan@wadolire.com.au
www.wadolcare.com.au
Linkora (details TBA)

include little icons beside the contact info:

- Envelope = email
- Phone = phone
- Globe = website

Font styles to use
Serif
Sans Serif

Requirements
Must have
• look proffesional and clean

```html
<!DOCTYPE html>
<html lang="en">
<head>
<meta charset="utf-8">
<title>Wadol Care – Business Card</title>
<link rel="stylesheet" href="https://fonts.googleapis.com/css2?family=Montserrat:wght@400;500;700;800&display=swap">
<style>
  :root {
    --backdrop: #3a3a3c;
    --card: #050505;
    --blue: #1d4f8f;
    --orange: #f19a24;
    --white: #ffffff;
    --muted: #e8e8e8;
  }
  * { margin: 0; padding: 0; box-sizing: border-box; }
  html, body {
    width: 1200px; height: 900px; overflow: hidden;
    background: var(--backdrop);
    font-family: "Montserrat", Arial, sans-serif;
  }
  .card {
    position: absolute; left: 250px;
    width: 700px; height: 400px;
    background: var(--card);
    border-radius: 22px;
    overflow: hidden;
    box-shadow: 0 10px 30px rgba(0,0,0,.45);
  }
  .card--front { top: 35px; }
  .card--back { top: 465px; }
  .card-shapes { position: absolute; inset: 0; width: 100%; height: 100%; }

  .wordmark { position: absolute; color: var(--blue); font-weight: 800; letter-spacing: -1px; line-height: 1; white-space: nowrap; }
  .card--front .wordmark { left: 0; right: 0; top: 140px; text-align: center; font-size: 82px; }
  .card--back .wordmark { left: 50px; top: 92px; font-size: 58px; display: flex; align-items: center; gap: 14px; }
  .wordmark-dot { width: 18px; height: 18px; border-radius: 50%; background: var(--orange); }

  .front-url { position: absolute; left: 28px; bottom: 14px; color: var(--white); font-size: 17px; font-weight: 500; }
  .front-url .accent, .contact .accent { color: var(--orange); font-weight: 700; }

  .person { position: absolute; right: 50px; top: 74px; text-align: right; }
  .person-name { color: var(--blue); font-size: 27px; font-weight: 700; }
  .person-role { color: var(--orange); font-size: 15px; font-weight: 500; margin-top: 2px; }

  .contacts { position: absolute; left: 50px; top: 258px; list-style: none; }
  .contact { display: flex; align-items: center; gap: 10px; color: var(--white); font-size: 17px; line-height: 24px; }
  .contact svg { width: 14px; height: 14px; flex: none; }

  .social { position: absolute; right: 24px; top: 228px; color: var(--white); font-size: 19px; font-weight: 500; display: flex; align-items: center; gap: 12px; }
  .social-dot { width: 12px; height: 12px; border-radius: 50%; background: var(--orange); }
</style>
</head>
<body>

<section class="card card--front" aria-label="Card front">
  <svg class="card-shapes" viewBox="0 0 700 400" aria-hidden="true">
    <polygon points="0,350 240,350 272,400 0,400" fill="var(--blue)"/>
    <polygon points="250,352 700,326 700,334 258,360" fill="var(--orange)"/>
  </svg>
  <div class="wordmark">wadol care</div>
  <div class="front-url">www.<span class="accent">wadolcare</span>.com.au</div>
</section>

<section class="card card--back" aria-label="Card back">
  <svg class="card-shapes" viewBox="0 0 700 400" aria-hidden="true">
    <line x1="650" y1="140" x2="50" y2="248" stroke="var(--white)" stroke-width="2"/>
    <polygon points="600,215 700,215 700,285 575,285" fill="var(--blue)"/>
    <polygon points="30,372 520,372 560,300 568,300 527,380 30,380" fill="var(--orange)"/>
  </svg>

  <div class="wordmark"><span>wadol care</span><span class="wordmark-dot"></span></div>

  <div class="person">
    <div class="person-name">Tovan Brelsick</div>
    <div class="person-role">Director</div>
  </div>

  <ul class="contacts">
    <li class="contact">
      <svg viewBox="0 0 24 24"><path fill="var(--orange)" d="M6.6 10.8a15 15 0 0 0 6.6 6.6l2.2-2.2c.3-.3.7-.4 1-.2 1.1.4 2.3.6 3.6.6.6 0 1 .4 1 1V20c0 .6-.4 1-1 1A17 17 0 0 1 3 4c0-.6.4-1 1-1h3.5c.6 0 1 .4 1 1 0 1.3.2 2.5.6 3.6.1.3 0 .7-.2 1z"/></svg>
      0427 31 64 92 (larger)
    </li>
    <li class="contact">
      <svg viewBox="0 0 24 24"><rect x="6" y="2" width="12" height="20" rx="2" fill="none" stroke="var(--orange)" stroke-width="2.4"/><circle cx="12" cy="18" r="1.4" fill="var(--orange)"/></svg>
      1300 73 29 41
    </li>
    <li class="contact">
      <svg viewBox="0 0 24 24"><rect x="2" y="5" width="20" height="14" rx="1.5" fill="none" stroke="var(--orange)" stroke-width="2.4"/><path d="M2 6l10 7 10-7" fill="none" stroke="var(--orange)" stroke-width="2.4"/></svg>
      tovan@wadolire.com.au
    </li>
    <li class="contact">
      <svg viewBox="0 0 24 24"><circle cx="12" cy="12" r="9.5" fill="none" stroke="var(--orange)" stroke-width="2.2"/><path d="M2.5 12h19M12 2.5c3 3 3 16 0 19M12 2.5c-3 3-3 16 0 19" fill="none" stroke="var(--orange)" stroke-width="1.8"/></svg>
      <span>www.<span class="accent">wadolcare.com</span>.au</span>
    </li>
  </ul>

  <div class="social">Linkora /TBA.com <span class="social-dot"></span></div>
</section>

</body>
</html>
```